New Townhome community needs for sale sign.

need a 4 foot by 8 foot banner to put on building listing newly constructed townhomes as "coming soon" to market. Construction is scheduled to be completed Dec 2024. Sale of units will begin Spring of 2025.
6 individual townhome units each 2,000 square feet. each unit is 3 bedroom 2.5 bathroom with 2 car garage and each has a rooftop "sky lounge" with amazing views. Gated community. Units available for sale Spring of 2025. Real estate company selling units will be Norvale & Partners. Will need Norvale & Partners Logo on the banner. Would like to keep with the same blue color scheme as the Norvale & Partners logo. phone number on banner to be 602-555-4179. web norvalex.com.

```html
<!DOCTYPE html>
<html lang="en">
<head>
<meta charset="utf-8">
<title>Norvale &amp; Partners – Townhomes For Sale Banner</title>
<link href="https://fonts.googleapis.com/css2?family=Montserrat:wght@600;800&family=Oswald:wght@500&family=Roboto:wght@400&display=swap" rel="stylesheet">
<style>
  :root {
    --stage: #e9edf1;
    --paper: #f3f4f6;
    --navy: #1b6398;
    --sky-blue: #2a8cc6;
    --ink: #1d1f22;
    --white: #ffffff;
  }
  * { box-sizing: border-box; margin: 0; padding: 0; }
  html, body { width: 1200px; height: 960px; overflow: hidden; background: var(--stage); }
  .banner {
    position: absolute; left: 40px; top: 200px;
    width: 1120px; height: 560px;
    display: flex; box-shadow: 0 10px 30px rgba(0,0,0,.15);
  }
  .info { width: 500px; background: var(--paper); display: flex; flex-direction: column; }
  .brand { height: 128px; display: flex; align-items: center; gap: 14px; padding-left: 56px; padding-top: 8px; }
  .brand-mark { width: 50px; height: 50px; background: var(--sky-blue); }
  .brand-name { font-family: "Montserrat", sans-serif; font-weight: 600; font-size: 30px; color: var(--navy); white-space: nowrap; }
  .headline {
    height: 118px; background: var(--navy); color: var(--white);
    font-family: "Montserrat", sans-serif; font-weight: 800; font-size: 72px; letter-spacing: 2px;
    display: flex; align-items: center; padding-left: 56px;
  }
  .details {
    flex: 1; padding: 22px 40px 0 56px;
    font-family: "Roboto", sans-serif; font-size: 15.5px; line-height: 1.38; color: var(--ink);
  }
  .contact {
    height: 170px; background: var(--sky-blue); color: var(--white);
    padding: 28px 0 0 56px; display: flex; flex-direction: column; gap: 12px;
  }
  .contact-row { display: flex; align-items: center; gap: 14px; }
  .contact-row svg { width: 40px; height: 40px; flex: none; }
  .phone { font-family: "Oswald", sans-serif; font-weight: 500; font-size: 54px; letter-spacing: 5px; line-height: 1; }
  .web { font-family: "Roboto", sans-serif; font-size: 44px; line-height: 1; white-space: nowrap; }
  .photo {
    flex: 1;
    background: linear-gradient(180deg, #2f78c9 0%, #6aa4d8 22%, #d9b9a4 45%, #c9a48c 65%, #a3836f 85%, #c2bcb4 100%);
  }
</style>
</head>
<body>
  <main class="banner">
    <section class="info">
      <header class="brand">
        <span class="brand-mark"></span>
        <span class="brand-name">Norvale &amp; Partners</span>
      </header>
      <h1 class="headline">FOR SALE</h1>
      <p class="details">6 individual townhome units each 2,000 square feet. each unit is 3 bedroom 2.5 bathroom with 2 car garage and each has a rooftop "sky lounge" with amazing views. Gated community. Units available for sale Spring of 2025. Real estate company selling units will be Norvale &amp; Partners</p>
      <footer class="contact">
        <div class="contact-row">
          <svg viewBox="0 0 24 24" fill="none" stroke="currentColor" stroke-width="1.6" stroke-linecap="round" stroke-linejoin="round">
            <path d="M5 3h3.5l1.8 4.5-2.3 1.4a11 11 0 0 0 5.1 5.1l1.4-2.3L19 13.5V17a2 2 0 0 1-2 2A15 15 0 0 1 3 5a2 2 0 0 1 2-2z"/>
            <path d="M14.5 3.5a6 6 0 0 1 6 6M14.5 7a2.5 2.5 0 0 1 2.5 2.5"/>
          </svg>
          <span class="phone">602-555-4179</span>
        </div>
        <div class="contact-row">
          <svg viewBox="0 0 24 24" fill="none" stroke="currentColor" stroke-width="1.6">
            <circle cx="12" cy="12" r="9"/>
            <ellipse cx="12" cy="12" rx="4" ry="9"/>
            <path d="M3 12h18M4.5 7.5h15M4.5 16.5h15"/>
          </svg>
          <span class="web">norvalex.com.</span>
        </div>
      </footer>
    </section>
    <div class="photo" role="img" aria-label="Photo of a stucco home with tiled roof, two-car garage, desert landscaping and a tree under blue sky"></div>
  </main>
</body>
</html>
```